Rug Cleaning Web Design Project

We need a web design for our cleaning company. We currently have a web page but are not happy with its design. We currently offer fine rug cleaning,upholstery cleaning, and residential and commercial carpet cleanning. We also offer water damage restoration. For our rug cleaning services we offer : Enzyme treatments for pet contamination and odor removal, application of stain protection that is designed for the fine textiles used in rug construction, application of treatments designed to prevent moth damage and pads designed to be used under rugs.Our current web site is harborfreshcare.example. We are intrested in a design with similar information to the web page of Velmora Rug Cleaners INC. We would like to use the colors that are present in our logo that will be uploaded with this description. We would also like this new page to be linked to our other address loomrinsepro.example. We would like the deign to be visually attractive but not "too busy".
Updates

Please include pictures of rugs, or people washing rugs if possible. We do not offer maid type cleaning services. We would not be interested in designs including pictures depicting that type service. Thanks for your hard work on this project.

Dana Whitlow

Industry/Entity Type

Residential

Requirements
Must have
• This page must be viewable on smart phones and tablets.

```html
<!DOCTYPE html>
<html lang="en">
<head>
<meta charset="utf-8">
<meta name="viewport" content="width=device-width, initial-scale=1">
<title>LoomRinsePro – Harbor Fresh Care</title>
<link href="https://fonts.googleapis.com/css2?family=PT+Sans:wght@400;700&display=swap" rel="stylesheet">
<style>
  :root {
    --ink: #2b2b2b;
    --grey-text: #6f6f6f;
    --nav-blue: #1b3d73;
    --accent: #2a8fd0;
    --button-top: #7fcdf3;
    --button-bottom: #4fb2e6;
    --panel: #f2f2f2;
    --panel-edge: #dfe7ed;
    --sky-top: #ffffff;
    --sky-bottom: #8ccbef;
    --card-top: #6cc0ec;
    --card-bottom: #3a9bd0;
    --card-text: #13314f;
  }
  * { box-sizing: border-box; margin: 0; padding: 0; }
  html, body { width: 1200px; height: 844px; overflow: hidden; }
  body {
    font-family: "PT Sans", Tahoma, sans-serif;
    background: linear-gradient(to bottom, var(--sky-top) 0, var(--sky-top) 400px, #dff0fb 520px, var(--sky-bottom) 844px);
    position: relative;
    color: var(--ink);
  }
  .brand {
    position: absolute; left: 150px; top: 58px;
    display: flex; align-items: center; gap: 12px;
    font-size: 38px; font-weight: 700; color: #1f1f1f; letter-spacing: -1px;
  }
  .brand-dot {
    width: 46px; height: 46px; border-radius: 50%;
    background: var(--accent);
  }
  .main-nav {
    position: absolute; top: 80px; right: 150px;
    display: flex; align-items: center; gap: 20px;
  }
  .main-nav a {
    font-size: 14px; color: var(--nav-blue); text-decoration: none;
    padding: 7px 12px; letter-spacing: .3px;
  }
  .main-nav a:last-child { padding-right: 0; }
  .main-nav a.is-current {
    background: linear-gradient(var(--button-top), var(--button-bottom));
    border: 1px solid #8fd2f2; border-radius: 4px;
    box-shadow: 0 1px 2px rgba(0,0,0,.15);
  }
  .hero { position: absolute; left: 150px; top: 144px; width: 900px; height: 300px; }
  .hero svg { position: absolute; left: 0; top: 0; }
  .hero-copy {
    position: absolute; right: 45px; top: 44px; width: 520px;
    text-align: right; color: var(--grey-text);
  }
  .hero-title { font-size: 25px; font-weight: 400; color: #7a7a7a; margin-bottom: 28px; }
  .hero-text { font-size: 14px; line-height: 28px; }
  .hero-text .award { color: var(--accent); font-size: 18px; }
  .hero-dots { position: absolute; right: 47px; top: 215px; display: flex; gap: 9px; }
  .hero-dots span {
    width: 12px; height: 12px; border-radius: 50%;
    background: linear-gradient(#fafafa, #d7d7d7); border: 1px solid #c4c4c4;
  }
  .hero-dots span.is-active { background: radial-gradient(circle at 40% 35%, #6cc4f0, #1f78b8); border-color: #1f78b8; }
  .water-splash {
    position: absolute; left: 620px; top: 372px; width: 580px; height: 130px;
    background: radial-gradient(ellipse at 60% 60%, rgba(64,160,215,.55), rgba(140,205,240,.25) 55%, rgba(255,255,255,0) 75%);
  }
  .features { position: absolute; left: 150px; top: 526px; display: flex; gap: 19px; }
  .feature { width: 211px; }
  .feature h2 { font-size: 16px; font-weight: 400; color: var(--ink); margin-bottom: 11px; height: 20px; }
  .feature-photo { width: 211px; height: 112px; margin-bottom: 13px; }
  .photo-rug { background: linear-gradient(135deg, #cdbb9c, #a8987c); }
  .photo-water { background: linear-gradient(135deg, #e4eaf0, #9eb0c2); }
  .photo-carpet { background: linear-gradient(135deg, #6fb6e4, #2f7fc0); }
  .feature p { font-size: 11.5px; line-height: 17px; color: var(--grey-text); }
  .contact-card {
    width: 211px; height: 171px; border-radius: 5px;
    background: linear-gradient(var(--card-top), var(--card-bottom));
    border: 1px solid #8fd0f0;
    padding: 14px 16px; color: var(--card-text);
    font-size: 11.5px; line-height: 17px;
  }
  .contact-card .phone { margin-top: 9px; font-size: 11.5px; }
  .contact-card .phone strong { font-size: 18px; font-weight: 400; }
  .site-footer {
    position: absolute; left: 154px; right: 150px; top: 803px;
    display: flex; justify-content: space-between;
    font-size: 11.5px; color: var(--nav-blue);
  }
  .site-footer nav span { margin: 0 10px; }
</style>
</head>
<body>
  <header>
    <div class="brand"><span class="brand-dot"></span>LoomRinsePro</div>
    <nav class="main-nav">
      <a href="#" class="is-current">Home</a>
      <a href="#">About Us</a>
      <a href="#">Rug Washing</a>
      <a href="#">Water Damage</a>
      <a href="#">Carpet Cleaning</a>
    </nav>
  </header>

  <div class="water-splash" role="img" aria-label="Splash of water with bubbles flowing from the banner"></div>

  <section class="hero">
    <svg width="900" height="300" viewBox="0 0 900 300">
      <defs>
        <clipPath id="hero-shape">
          <path d="M0 0 H900 V240 Q900 258 872 263 Q640 302 430 283 Q140 268 22 250 Q0 246 0 228 Z"/>
        </clipPath>
        <linearGradient id="photo-fade" x1="0" x2="1">
          <stop offset="0" stop-color="#b9c4cc"/>
          <stop offset=".55" stop-color="#d6dce0"/>
          <stop offset="1" stop-color="#f2f2f2"/>
        </linearGradient>
      </defs>
      <path d="M0 0 H900 V240 Q900 258 872 263 Q640 302 430 283 Q140 268 22 250 Q0 246 0 228 Z" fill="var(--panel)" stroke="var(--panel-edge)" stroke-width="6"/>
      <g clip-path="url(#hero-shape)" role="img" aria-label="Technician in a blue shirt cleaning carpet with a wand">
        <rect x="0" y="0" width="440" height="300" fill="url(#photo-fade)"/>
      </g>
    </svg>
    <div class="hero-copy">
      <h1 class="hero-title">Rug washing Pro</h1>
      <p class="hero-text">LoomRinsePro &amp; Restoration is the recipient of the 2010 &amp; 2011<br>
        <span class="award">"Best in Business Award"</span> in Huntsville, Alabama for Water Damage<br>
        Restoration and Carpet and Rug Cleaning.</p>
    </div>
    <div class="hero-dots"><span></span><span></span><span></span><span class="is-active"></span></div>
  </section>

  <main class="features">
    <section class="feature">
      <h2>Contact Us</h2>
      <address class="contact-card" style="font-style:normal">
        Harbor Fresh Care &amp; Restoration<br>
        48 Fenwick Lane<br>
        Cedar Hollow, AL &nbsp;35000<br>
        Serving Huntsville and surrounding areas.
        <div class="phone">Phone: <strong>(555) 014-2290</strong><br>office@harborfreshcare.example</div>
      </address>
    </section>
    <section class="feature">
      <h2>Rug washing</h2>
      <div class="feature-photo photo-rug" role="img" aria-label="Cleaning wand moving over a beige rug"></div>
      <p>Oriental and Speciality Rugs differ greatly in their construction, dyeing methods and fiber content.</p>
    </section>
    <section class="feature">
      <h2>Water Damage</h2>
      <div class="feature-photo photo-water" role="img" aria-label="Radiator valve on pipes"></div>
      <p>Trust the company that has been getting families back home and businesses back to work for over 20 years.</p>
    </section>
    <section class="feature">
      <h2>Carpet Cleaning</h2>
      <div class="feature-photo photo-carpet" role="img" aria-label="Vacuum nozzle on a blue carpet"></div>
      <p>Oriental and Speciality Rugs differ greatly in their construction, dyeing methods and fiber content.</p>
    </section>
  </main>

  <footer class="site-footer">
    <span>LoomRinsePro.2012 All rights reserved</span>
    <nav>Terms &amp; Condition<span>|</span>Privacy Policy</nav>
  </footer>
</body>
</html>
```